Newsletter-Design für Print - tornhof partner
Zielgruppe
tornhof partner business hat sich auf die Kaltakquise und den Vertrieb spezialisiert. Generell agieren wir ausschließlich im BtoB Bereich überwiegend für die Industrie.
Aufgabenstellung
verwenden unserer Logofarben - Blau und Rot - maximal noch grau - sehr puristisch und minimalistisch - klare Struktur für case studiens - checklisten - whitepapers

```html
<!DOCTYPE html>
<html lang="de">
<head>
<meta charset="utf-8">
<title>Newsletter – tornhof partner</title>
<link href="https://fonts.googleapis.com/css2?family=Exo+2:wght@300;400;500;700&display=swap" rel="stylesheet">
<style>
:root{
  --red:#cf161b;
  --red-dark:#a51014;
  --blue:#0d4885;
  --grey:#6f6f6f;
  --ink:#1a1a1a;
  --white:#ffffff;
}
*{margin:0;padding:0;box-sizing:border-box}
html,body{width:848px;height:1200px;overflow:hidden;background:var(--white)}
body{font-family:"Exo 2",sans-serif;position:relative}
.masthead{position:absolute;left:0;top:0;width:848px;height:344px;background:var(--red);overflow:hidden}
.masthead-photo{position:absolute;inset:0;background:radial-gradient(ellipse at 60% 30%,#e0262b 0%,#c41419 45%,#9e0f13 100%)}
.issue{position:absolute;left:25px;top:12px;color:var(--white);font-size:24px;font-weight:400}
.title{position:absolute;left:26px;top:196px;color:var(--white);font-size:121px;font-weight:700;line-height:1;letter-spacing:0.5px}
.lead-headline{position:absolute;left:39px;top:392px;color:var(--red);font-size:41px;font-weight:700;line-height:47px;white-space:nowrap}
.copy{position:absolute;color:var(--grey);font-size:13.4px;font-weight:300;line-height:20px;text-align:justify;text-align-last:justify;hyphens:manual}
.copy.end{text-align-last:left}
.pullquote{position:absolute;left:172px;top:678px;width:310px;color:var(--ink);font-size:27px;font-weight:400;line-height:31px;white-space:nowrap}
.teaser{position:absolute;left:606px;width:202px}
.teaser h2{color:var(--blue);font-size:25px;font-weight:700;line-height:31px}
.teaser p{margin-top:6px;color:var(--grey);font-size:13.4px;font-weight:300;line-height:20px;text-align:justify;text-align-last:left}
.teaser .page{display:block;text-align:right;color:var(--blue);font-size:14px;font-weight:500;line-height:20px;margin-top:2px}
.dots{position:absolute;height:3px;background-image:radial-gradient(circle,var(--ink) 1.1px,transparent 1.3px);background-size:5px 3px}
.brand{position:absolute;left:0;width:848px;top:1128px;text-align:center;color:var(--blue);font-size:32px;font-weight:500;letter-spacing:0.5px}
.footer-band{position:absolute;left:0;top:1180px;width:848px;height:20px;background:var(--red)}
</style>
</head>
<body>
<header class="masthead">
  <div class="masthead-photo" role="img" aria-label="Foto: Team im Büro, rot eingefärbt"></div>
  <div class="issue">No 01 / Oktober 2017</div>
  <div class="title">NEWSLETTER</div>
</header>

<h1 class="lead-headline">Hier Platz für eine<br>Headline lorem ipsum est</h1>

<div class="copy" style="left:40px;top:489px;width:261px">Lorem ipsum dolor sit amet, consectetu­er adipiscing elit. Aenean commodo ligula eget dolor. Aenean massa. Cum sociis na­toque penatibus et magnis dis parturient montes, nascetur ridiculus mus. Donec quam felis, ultricies nec, pellentesque eu, pretium quis, sem. Nulla consequat mas-</div>
<div class="copy" style="left:40px;top:629px;width:107px">sa quis enim. Donec pede justo, fringilla vel, aliquet nec, vulputate eget, arcu. In enim justo, rhoncus ut, imperdiet a, venenatis vitae, justo. Nullam dictum felis eu</div>
<div class="copy end" style="left:40px;top:849px;width:261px">pede mollis pretium. Integer tincidunt. Cras dapibus. Vivamus elementum sem­per nisi. Aenean vulputate eleifend tellus. Aenean leo ligula, porttitor eu, consequat vitae, eleifend ac, enim.</div>
<div class="copy" style="left:40px;top:969px;width:261px">Aliquam lorem ante, dapibus in, viverra quis, feugiat a, tellus. Phasellus viverra nulla ut metus varius laoreet. Quisque rutrum. Aenean imperdiet. Etiam ultricies</div>

<div class="copy" style="left:321px;top:489px;width:260px">nisi vel augue. Curabitur ullamcorper ul­tricies nisi. Nam eget dui. Etiam rhoncus. Maecenas tempus, tellus eget condimen­tum rhoncus, sem quam semper libero, sit amet adipiscing sem neque sed ipsum. Nam quam nunc, blandit vel, luctus pul­vinar, hendrerit id, lorem. Maecenas nec</div>
<div class="copy" style="left:489px;top:629px;width:92px">odio et ante tincidunt tem­pus. Donec vitae sapien ut libero vene­natis faucibus. Nullam quis ante. Etiam sit amet orci eget eros faucibus tincidunt. Duis</div>
<div class="copy end" style="left:321px;top:849px;width:260px">leo. Sed fringilla mauris sit amet nibh. Donec sodales sagittis magna.</div>
<div class="copy" style="left:321px;top:927px;width:260px">Sed consequat, leo eget bibendum so­dales, augue velit cursus nunc, Lorem ipsum dolor sit amet, consectetuer adi­piscing elit. Aenean commodo ligula eget dolor. Aenean massa. Cum sociis natoque penatibus et magnis dis parturient mon­tes, nascetur sodales, augue velit cursus</div>

<blockquote class="pullquote">„Zitat aus dem Artikel<br>dolor sit amet, consec-<br>tetuer adipiscing elit.<br>Aenean commodo ligu-<br>la eget dolor est.</blockquote>

<article class="teaser" style="top:510px">
  <h2>Thema 01<br>Headline lorem</h2>
  <p>Lorem ipsum dolor sit amet, consectetuer adipiscing elit. Aenean commodo ligula eget dolor. Aenean massa</p>
  <span class="page">Seite 02</span>
</article>
<div class="dots" style="left:606px;top:687px;width:203px"></div>
<article class="teaser" style="top:712px">
  <h2>Thema 02<br>Headline lorem</h2>
  <p>Lorem ipsum dolor sit amet, consectetuer adipiscing elit. Aenean commodo ligula eget dolor. Aenean massa</p>
  <span class="page">Seite 04</span>
</article>
<div class="dots" style="left:606px;top:887px;width:203px"></div>
<article class="teaser" style="top:914px">
  <h2>Thema 03<br>Headline lorem</h2>
  <p>Lorem ipsum dolor sit amet, consectetuer adipiscing elit. Aenean commodo ligula eget dolor. Aenean massa</p>
  <span class="page">Seite 06</span>
</article>

<div class="dots" style="left:39px;top:1107px;width:774px"></div>
<div class="brand">tornhof partner</div>
<div class="footer-band"></div>
</body>
</html>
```